Esthetically Pleasing Core Values and Brand Promise for Accounting Firm

I would like a cohesive design that ties together my core values and brand promise. My firm, Maple Finch Advisory, provides accounting work to small businesses. I prefer modern and clean designs. I want my Core Values and Brand Promise to represent me - sole entrepreneur, married, mother of two kids, modern esthetics, clean lines, organized, colorful (teals, greys, white, yellows)

Industry/Entity Type

Public Accounting

Colors
33b8a4

```html
<!DOCTYPE html>
<html lang="en">
<head>
<meta charset="utf-8">
<title>Maple Finch Advisory – Core Values and Brand Promise</title>
<link rel="stylesheet" href="https://fonts.googleapis.com/css2?family=Montserrat:wght@600;700;800&family=Open+Sans:wght@400;600&display=swap">
<style>
  :root{
    --teal:#33b8a4;
    --teal-dark:#23998a;
    --teal-pale:#e3f5f1;
    --yellow:#fcd423;
    --ink:#2b2b2b;
    --grey:#d9dcdc;
    --grey-light:#f1f2f2;
    --page:#eceeee;
    --white:#ffffff;
  }
  *{box-sizing:border-box;margin:0;padding:0}
  html,body{width:1200px;height:2564px;overflow:hidden;background:var(--page)}
  .poster{
    position:absolute;left:50px;top:432px;width:1100px;height:1700px;
    background:var(--white);overflow:hidden;
    box-shadow:0 6px 30px rgba(0,0,0,.12);
  }
  .poster__tint{
    position:absolute;left:0;top:0;width:100%;height:1000px;
    background:linear-gradient(160deg,var(--grey-light) 0%,var(--white) 45%);
  }
  .core-title{
    position:absolute;left:60px;top:70px;height:880px;width:120px;
    writing-mode:vertical-rl;transform:rotate(180deg);
    white-space:nowrap;
    font-family:"Montserrat",sans-serif;font-weight:800;font-size:90px;
    letter-spacing:6px;text-align:center;line-height:120px;
  }
  .core-title__core{color:var(--teal)}
  .core-title__values{color:var(--yellow)}
  .values{position:absolute;left:230px;top:90px;width:820px}
  .value{position:relative;height:218px}
  .value__icon{
    position:absolute;left:0;top:0;width:84px;height:84px;background:var(--yellow);
    display:flex;align-items:center;justify-content:center;
  }
  .value__icon svg{width:54px;height:54px}
  .value__title{
    position:absolute;left:96px;top:6px;height:72px;width:560px;
    background:var(--teal);color:var(--white);
    clip-path:polygon(0 0,92% 0,100% 50%,92% 100%,0 100%,5% 50%);
    font-family:"Montserrat",sans-serif;font-weight:700;font-size:44px;
    line-height:72px;padding-left:58px;white-space:nowrap;
  }
  .value__text{
    position:absolute;left:0;top:100px;width:780px;padding:14px 24px;
    background:linear-gradient(90deg,var(--grey) 0%,var(--grey-light) 80%,rgba(255,255,255,0) 100%);
    clip-path:polygon(0 0,100% 0,96% 100%,0 100%);
    font-family:"Open Sans",sans-serif;font-weight:600;font-size:26px;line-height:36px;color:var(--ink);
  }
  .promise{
    position:absolute;left:0;top:1000px;width:100%;height:700px;background:var(--teal);
    text-align:center;
  }
  .promise__title{
    margin-top:50px;white-space:nowrap;
    font-family:"Montserrat",sans-serif;font-weight:800;font-size:104px;line-height:120px;color:var(--white);letter-spacing:2px;
  }
  .promise__tagline{
    display:inline-block;margin-top:20px;height:76px;padding:0 48px;border-radius:38px;background:var(--yellow);
    line-height:76px;white-space:nowrap;
    font-family:"Montserrat",sans-serif;font-weight:700;font-size:38px;color:var(--ink);
  }
  .promise__body{
    position:absolute;left:0;top:300px;width:100%;height:400px;background:var(--teal-pale);
    padding:50px 70px 0;text-align:left;
    font-family:"Open Sans",sans-serif;font-size:28px;line-height:40px;color:var(--ink);
  }
  .promise__body p{margin-bottom:28px}
  .promise__body strong{font-weight:600;color:var(--teal-dark)}
  .promise__wave{position:absolute;left:0;bottom:0;width:100%;height:80px}
</style>
</head>
<body>
<main class="poster">
  <div class="poster__tint"></div>

  <h1 class="core-title"><span class="core-title__core">CORE </span><span class="core-title__values">VALUES</span></h1>

  <section class="values">
    <article class="value">
      <div class="value__icon">
        <svg viewBox="0 0 24 24" fill="#2b2b2b"><circle cx="12" cy="7" r="3.2"/><path d="M5.5 19c0-3.6 2.9-6 6.5-6s6.5 2.4 6.5 6z"/><circle cx="4.5" cy="9" r="2"/><circle cx="19.5" cy="9" r="2"/></svg>
      </div>
      <h2 class="value__title">EMPOWER</h2>
      <p class="value__text">We are dedicated, appreciative and respectful of<br>people's time and purpose.</p>
    </article>
    <article class="value">
      <div class="value__icon">
        <svg viewBox="0 0 24 24" fill="none" stroke="#2b2b2b" stroke-width="2"><rect x="4" y="3" width="16" height="18" rx="1"/><path d="M7 8l1.5 1.5L11 7M7 14l1.5 1.5L11 13M13 8.5h4M13 14.5h4"/></svg>
      </div>
      <h2 class="value__title">CLIENT FOCUSED</h2>
      <p class="value__text">We provide a personal service that goes above the<br>standards of professional care.</p>
    </article>
    <article class="value">
      <div class="value__icon">
        <svg viewBox="0 0 24 24" fill="none" stroke="#2b2b2b" stroke-width="1.8"><path d="M12 3v17M7 20h10M4 6h16M6 6l-3 7h6zM18 6l-3 7h6z"/></svg>
      </div>
      <h2 class="value__title">RECTITUDE</h2>
      <p class="value__text">We know the difference between what we have the right<br>to do and what the right thing to do is.</p>
    </article>
    <article class="value">
      <div class="value__icon">
        <svg viewBox="0 0 24 24" fill="none" stroke="#2b2b2b" stroke-width="2"><circle cx="12" cy="12" r="8.5"/><circle cx="12" cy="12" r="4.5"/><circle cx="12" cy="12" r="1" fill="#2b2b2b"/></svg>
      </div>
      <h2 class="value__title">RELENTLESS</h2>
      <p class="value__text">We believe that the longer we try to do our best,<br>the better we become.</p>
    </article>
  </section>

  <section class="promise">
    <h2 class="promise__title">BRAND PROMISE</h2>
    <p class="promise__tagline">Trust, Transparency and Dependability</p>
    <div class="promise__body">
      <p><strong>Tax</strong> – Maple Finch Advisory provides all clients with a trusted tax advisor who provides accurate tax filings and ensures your compliance with all government agencies.</p>
      <p><strong>Accounting</strong> – Maple Finch Advisory provides all business owners with the financial visibility needed to foster growth and facilitate goals.</p>
      <svg class="promise__wave" viewBox="0 0 1100 80" preserveAspectRatio="none"><path d="M0 40 C300 0 700 80 1100 20 L1100 80 L0 80z" fill="#33b8a4"/></svg>
    </div>
  </section>
</main>
</body>
</html>
```